Digital Album Cover - Frosted Lanterns (Night Falls Still)

HiI need a digital album cover for a piano instrumental cover single

Artist: Corey Dalton
Title: Frosted Lanterns (Night Falls Still)

The song was originally by Derek Holloway

Please use my logo

You can listen to the track herehttps://soundcloud.com/coreydaltonkeys/frosted-lanterns-night-falls-still-piano-instrumental-cover

Requirements
Must have
• My logo design Corey Dalton

```html
<!DOCTYPE html>
<html lang="en">
<head>
<meta charset="utf-8">
<title>Frosted Lanterns (Night Falls Still) – Corey Dalton</title>
<link rel="stylesheet" href="https://fonts.googleapis.com/css2?family=Alfa+Slab+One&family=Kaushan+Script&family=Heebo:wght@600&display=swap">
<style>
  :root {
    --haze: #d9bf9f;
    --warm-glow: #c98a5c;
    --amber: #a85f38;
    --ember: #6b3a22;
    --key-silver: #7d8796;
    --rose: #b0605a;
    --night: #141a2a;
    --deep-navy: #0b1020;
    --ink: #05070d;
    --white: #ffffff;
    --title-shadow: #b8432f;
  }
  html, body {
    margin: 0;
    padding: 0;
    overflow: hidden;
    background: var(--ink);
  }
  .cover {
    position: relative;
    width: 1200px;
    height: 1200px;
    overflow: hidden;
  }
  .cover__backdrop {
    position: absolute;
    inset: 0;
    background:
      radial-gradient(ellipse 32% 26% at 4% 6%, rgba(217, 191, 159, 0.9), transparent 72%),
      radial-gradient(ellipse 9% 9% at 57% 84%, rgba(196, 96, 86, 0.55), transparent 75%),
      radial-gradient(ellipse 14% 12% at 50% 72%, rgba(176, 96, 90, 0.4), transparent 75%),
      radial-gradient(ellipse 10% 12% at 12% 34%, rgba(214, 140, 96, 0.45), transparent 75%),
      linear-gradient(132deg,
        transparent 0%, transparent 30%,
        rgba(125, 135, 150, 0.0) 36%,
        rgba(125, 135, 150, 0.35) 44%,
        rgba(160, 168, 180, 0.42) 50%,
        rgba(110, 120, 140, 0.3) 56%,
        rgba(20, 26, 42, 0.0) 64%, transparent 100%),
      linear-gradient(132deg,
        transparent 0%, transparent 52%,
        rgba(6, 8, 14, 0.55) 60%, rgba(6, 8, 14, 0.25) 66%,
        rgba(60, 72, 100, 0.3) 76%, transparent 90%),
      linear-gradient(128deg, transparent 0%, transparent 28%, rgba(30, 18, 14, 0.6) 36%, rgba(30, 18, 14, 0.0) 44%),
      linear-gradient(135deg, var(--warm-glow) 0%, var(--amber) 18%, var(--ember) 36%, var(--night) 62%, var(--deep-navy) 82%, var(--ink) 100%);
  }
  .cover__title {
    position: absolute;
    top: 186px;
    left: 0;
    right: 0;
    margin: 0;
    text-align: center;
    color: var(--white);
    font-weight: 400;
  }
  .cover__title-main {
    display: block;
    font-family: "Alfa Slab One", serif;
    font-size: 74px;
    line-height: 1;
    letter-spacing: 1px;
    text-shadow: 4px 4px 0 var(--title-shadow);
  }
  .cover__title-sub {
    display: block;
    margin-top: 8px;
    font-family: "Kaushan Script", cursive;
    font-size: 84px;
    line-height: 1.05;
  }
  .artist {
    position: absolute;
    left: 67px;
    top: 1006px;
    display: flex;
    align-items: center;
  }
  .artist__mark {
    width: 103px;
    height: 103px;
    border-radius: 50%;
    background: var(--white);
    flex: none;
  }
  .artist__text {
    margin-left: 15px;
    padding-top: 20px;
    color: var(--white);
  }
  .artist__name {
    display: block;
    font-family: "Heebo", sans-serif;
    font-weight: 600;
    font-size: 38px;
    line-height: 1;
    letter-spacing: 0.6px;
    text-transform: uppercase;
  }
  .artist__role {
    display: block;
    margin-top: 10px;
    margin-left: 36px;
    font-family: "Heebo", sans-serif;
    font-weight: 600;
    font-size: 19px;
    line-height: 1;
    letter-spacing: 0.3px;
  }
</style>
</head>
<body>
  <main class="cover">
    <div class="cover__backdrop" role="img" aria-label="Close-up photograph of piano keys running diagonally across the cover, in warm amber light fading to deep blue, with glowing festive bokeh sparks"></div>

    <h1 class="cover__title">
      <span class="cover__title-main">Frosted Lanterns</span>
      <span class="cover__title-sub">(Night Falls Still)</span>
    </h1>

    <div class="artist">
      <div class="artist__mark" aria-hidden="true"></div>
      <div class="artist__text">
        <span class="artist__name">Corey Dalton</span>
        <span class="artist__role">Wedding &amp; Event Pianist</span>
      </div>
    </div>
  </main>
</body>
</html>
```